Locksmith SmartPhone Web Design Project

I am a locksmith and focus on customers that use their smart phones to find me. I have a static web page that I created myself but it is horrible. See for yourself at www.brevalkeyworks.com.au

I want a cross-platform static site that simply shows the information and with the ability to change minor items like pricing. I want it to be compelling in its look and feel (not overwhelming) but simple. It must have a; click to call button; the ability to install a hit counter from pagetallyo.com; payment information just like the current graphic of card/cash/quidlo (orla/brixalonte only).

This will be hosted on my own server.
Updates

Hello Designers,

I have updated the brief in the must have and nice to have fields.

Thank you all,

Tom.

Hello to all Designers,

There is about 9 days left before the deadline. The overall level of competition is extremely high and I would like to thank all the designers who have submitted so far, 27 submissions in total so far. Excellent work.

If you have submitted already and wish to provide new designs, I am keen to see them. 

Hi guys, time is almost up. Please submit any new designs that you may have. The quality has been excellent so far.

Tom.

Target Market(s)

People who are locked out of their house/shop/office etc.

Industry/Entity Type

Locksmith

Requirements
Must have
• click to call button
hit counter from pagetallyo
payment graphic card/cash/quidlo (orla/brixalonte only)
cross platform compatibility smartphone/phablet
Single column page preferable, can have two columns.
Nice to have
• When the page loads regardless of the mobile device, all info should be presented. In other words no vertical or horizontal scroll bars.
Should not have
• hidden code, advertising, credits etc

```html
<!DOCTYPE html>
<html lang="en">
<head>
<meta charset="utf-8">
<title>Breval Keyworks – Lockout Service</title>
<link rel="stylesheet" href="https://fonts.googleapis.com/css2?family=Arimo:wght@400;700&display=swap">
<style>
  :root {
    --ink: #111111;
    --muted: #6b6b6b;
    --rule: #d9d9d9;
    --panel: #f1f1f1;
    --panel-edge: #cfcfcf;
    --call: #2aa3c9;
    --call-edge: #1f86a8;
    --white: #ffffff;
    --card-edge: #dddddd;
    --orla: #1a2a8c;
    --brix: #d8261c;
    --quidlo: #1f3f8f;
  }
  * { box-sizing: border-box; margin: 0; padding: 0; }
  html, body {
    width: 1200px;
    height: 2611px;
    overflow: hidden;
    background: var(--white);
    font-family: "Arimo", Arial, sans-serif;
    color: var(--ink);
  }
  .page { position: relative; width: 1200px; height: 2611px; }

  .brand {
    position: absolute;
    left: 62px; top: 70px;
    font-size: 200px;
    line-height: 205px;
    font-weight: 400;
    letter-spacing: -4px;
    color: var(--ink);
  }

  .service-title {
    position: absolute;
    left: 58px; top: 775px;
    width: 500px;
    font-size: 62px; line-height: 74px; font-weight: 700;
  }
  .service-rule {
    position: absolute;
    left: 58px; top: 993px;
    width: 490px; height: 3px;
    background: var(--rule);
  }
  .offer {
    position: absolute;
    left: 58px; top: 1075px;
    width: 520px;
    font-size: 60px; line-height: 74px; font-weight: 700;
  }
  .accept-label {
    position: absolute;
    left: 58px; top: 1350px;
    font-size: 56px; color: var(--muted);
  }

  .hero-photo {
    position: absolute;
    left: 658px; top: 756px;
    width: 487px; height: 753px;
    background: linear-gradient(160deg, #8f9498 0%, #6d6a66 35%, #b07a5a 60%, #c9707a 80%, #7c8185 100%);
  }

  .pay-card {
    position: absolute;
    height: 160px;
    border: 3px solid var(--card-edge);
    background: var(--white);
    display: flex; align-items: center; justify-content: center;
    font-weight: 700;
  }
  .pay-orla { left: 58px; top: 1455px; width: 180px; font-size: 58px; color: var(--orla); }
  .pay-brix { left: 252px; top: 1470px; width: 190px; height: 130px; font-size: 32px; color: var(--brix); }
  .pay-cash {
    position: absolute;
    left: 58px; top: 1636px;
    width: 180px; height: 165px;
    background: linear-gradient(135deg, #9bbf86 0%, #5f8f52 55%, #3f6b3a 100%);
  }
  .pay-quidlo {
    position: absolute;
    left: 262px; top: 1695px;
    font-size: 44px; font-weight: 700; color: var(--quidlo);
  }

  .call-panel {
    position: absolute;
    left: 58px; top: 1829px;
    width: 1087px; height: 378px;
    background: var(--panel);
    border: 3px solid var(--panel-edge);
  }
  .call-button {
    position: absolute;
    left: 77px; top: 73px;
    width: 934px; height: 226px;
    background: var(--call);
    border: 3px solid var(--call-edge);
    border-radius: 6px;
    color: var(--ink);
    font-size: 72px; font-weight: 700;
    display: flex; align-items: center; justify-content: center;
    text-decoration: none;
  }

  .footer-rule {
    position: absolute;
    left: 0; top: 2356px;
    width: 1200px; height: 3px;
    background: var(--rule);
  }
  .footer-details {
    position: absolute;
    left: 0; top: 2435px;
    width: 1200px;
    text-align: center;
    font-size: 54px; line-height: 91px;
    color: var(--ink);
  }
</style>
</head>
<body>
<main class="page">
  <header class="brand">Breval<br>Keyworks</header>

  <h2 class="service-title">Lockout<br>Service</h2>
  <div class="service-rule"></div>
  <p class="offer">Locked out?<br>$150 Gets You<br>In. EASY!</p>

  <div class="hero-photo" role="img" aria-label="Photo of a padlock and heavy chain securing a metal gate"></div>

  <p class="accept-label">We Accept</p>
  <div class="pay-card pay-orla">orla</div>
  <div class="pay-card pay-brix">brixalonte</div>
  <div class="pay-cash" role="img" aria-label="Photo of a stack of banknotes, cash accepted"></div>
  <div class="pay-quidlo">quidlo</div>

  <section class="call-panel">
    <a class="call-button" href="tel:">Call Us Now!</a>
  </section>

  <div class="footer-rule"></div>
  <footer class="footer-details">
    ABN: 51702846139<br>
    Master Licence: 386214057
  </footer>
</main>
</body>
</html>
```